Business Card Design Project

Bold, modern, clean business card design needed. Prefer double sided with art logo on the back. Front of card with company name logo, no art.

Target Market(s)

Our consulting company supports local, state and federal law enforcement officers. Therefore the design should be clean and direct with no flash or arrogance to it.

Industry/Entity Type

Business

```html
<!DOCTYPE html>
<html lang="en">
<head>
<meta charset="UTF-8">
<title>Corvan Systems — Business Cards</title>
<link rel="stylesheet" href="https://fonts.googleapis.com/css2?family=Noto+Serif:ital,wght@0,400;0,700;1,400&display=swap">
<style>
  :root {
    --bg: #5a5d61;
    --card: #f3f3f3;
    --ink: #222222;
    --ink-soft: #333333;
    --green: #8cc21e;
  }
  * { margin: 0; padding: 0; box-sizing: border-box; }
  html, body { width: 1200px; height: 900px; overflow: hidden; }
  body {
    background: var(--bg);
    font-family: "Noto Serif", Georgia, serif;
    display: flex;
    flex-direction: column;
    align-items: center;
    justify-content: center;
    gap: 60px;
  }
  .card {
    width: 560px;
    height: 320px;
    background: var(--card);
    border-radius: 28px;
    box-shadow: 0 10px 30px rgba(0,0,0,0.35);
    position: relative;
  }
  .card-back {
    display: flex;
    align-items: center;
    justify-content: center;
  }
  .brand {
    display: flex;
    align-items: center;
    gap: 14px;
  }
  .brand-mark {
    width: 22px;
    height: 22px;
    border-radius: 50%;
    background: var(--green);
    flex: none;
  }
  .brand-name {
    font-weight: 700;
    color: var(--ink);
    letter-spacing: 0.04em;
  }
  .card-back .brand-name { font-size: 44px; }
  .card-front .brand {
    position: absolute;
    left: 48px;
    top: 104px;
  }
  .card-front .brand-name {
    font-size: 28px;
    line-height: 1.1;
  }
  .card-front .brand-mark { width: 18px; height: 18px; }
  .contact {
    position: absolute;
    right: 44px;
    top: 96px;
    width: 260px;
    text-align: right;
  }
  .person-name {
    font-size: 30px;
    color: var(--ink-soft);
    line-height: 1.1;
  }
  .person-role {
    font-size: 20px;
    font-style: italic;
    color: var(--green);
    margin-bottom: 22px;
  }
  .details { list-style: none; }
  .details li {
    display: flex;
    align-items: center;
    justify-content: flex-end;
    gap: 10px;
    font-size: 16px;
    color: var(--ink);
    line-height: 1.6;
    white-space: nowrap;
  }
  .details svg { width: 14px; height: 14px; flex: none; }
</style>
</head>
<body>
  <section class="card card-back" aria-label="Card back">
    <div class="brand">
      <span class="brand-mark"></span>
      <span class="brand-name">Corvan Systems</span>
    </div>
  </section>

  <section class="card card-front" aria-label="Card front">
    <div class="brand">
      <span class="brand-mark"></span>
      <span class="brand-name">Corvan<br>Systems</span>
    </div>
    <div class="contact">
      <p class="person-name">Daniel Reyes</p>
      <p class="person-role">Director</p>
      <ul class="details">
        <li>
          <svg viewBox="0 0 14 14" aria-hidden="true"><rect x="4" y="1" width="6" height="12" rx="1.2" fill="var(--green)"/><rect x="5.2" y="2.5" width="3.6" height="5" fill="#fff"/></svg>
          <span>314 720 596</span>
        </li>
        <li>
          <svg viewBox="0 0 14 14" aria-hidden="true"><rect x="1" y="3" width="12" height="8" fill="var(--green)"/><path d="M1 3 L7 8 L13 3" fill="none" stroke="#fff" stroke-width="1.2"/></svg>
          <span>info@corvansystems.ca</span>
        </li>
        <li>
          <svg viewBox="0 0 14 14" aria-hidden="true"><circle cx="7" cy="7" r="5.5" fill="none" stroke="var(--green)" stroke-width="1.3"/><ellipse cx="7" cy="7" rx="2.3" ry="5.5" fill="none" stroke="var(--green)" stroke-width="1.1"/><line x1="1.5" y1="7" x2="12.5" y2="7" stroke="var(--green)" stroke-width="1.1"/></svg>
          <span>www.corvan.ca</span>
        </li>
      </ul>
    </div>
  </section>
</body>
</html>
```